Recycling and Rubbish services for Residential and Commercial customers

We are after a complete redesign or freshening up of our current website.
www.trevlok.co.nz
On this site the general public can rent or buy rollaTUBs or skips for rubbish and recycling collection around the Nelson and Tasman area of New Zealand.

Target Market(s)

18 to 100 year old males and females in Nelson and Tasman area of New Zealand

Industry/Entity Type

Waste Management

Contact Information for Business Card

logo name title email phone web site address all the normal stuff

Number of Pages Required

5+ page

Colors

Designer to choose colors to be used in the design.

Requirements
Must have
• Has to be very fast and easy for the customer to rent bin, skip, tags, liner etc..
• see web site www.trevlok.co.nz
• An address finder so we can show two rates for urban and rural streets
Nice to have
• "We’re trying to get back to a more human face. Our customers appreciate that we are locals too. We are proud to be able to support our local community through sponsorship and donations."

```html
<!DOCTYPE html>
<html lang="en">
<head>
<meta charset="utf-8">
<title>Tidy Tub – Recycling and Rubbish Services</title>
<link rel="stylesheet" href="https://fonts.googleapis.com/css2?family=Lato:wght@400;700&family=Nunito+Sans:wght@700;800&family=Roboto+Condensed:wght@700&display=swap">
<style>
  :root {
    --brand-green: #0d5a2a;
    --brand-green-dark: #0a4620;
    --ink: #2b2b2b;
    --muted-line: #cfcfcf;
    --panel: #f3f3f3;
    --field: #fafafa;
    --field-border: #cdcdcd;
    --hero-fill: #4f7fb8;
    --white: #ffffff;
  }
  * { box-sizing: border-box; margin: 0; padding: 0; }
  html, body { width: 859px; height: 1200px; overflow: hidden; background: var(--white); }
  body { position: relative; font-family: "Lato", Arial, sans-serif; color: var(--ink); }

  .brand { position: absolute; display: flex; align-items: center; gap: 6px; }
  .brand-mark { width: 14px; height: 14px; background: var(--brand-green); }
  .brand-name { font-family: "Nunito Sans", Arial, sans-serif; font-weight: 800; color: var(--brand-green); font-size: 22px; letter-spacing: 0.5px; }
  .site-header .brand { left: 33px; top: 42px; }

  .info-band { position: absolute; left: 480px; top: 10px; width: 352px; height: 26px; }
  .info-band svg.band { position: absolute; inset: 0; }
  .info-content { position: absolute; inset: 0; display: flex; align-items: center; padding-left: 38px; color: var(--white); font-family: "Nunito Sans", Arial, sans-serif; font-weight: 800; font-size: 10.5px; letter-spacing: 0.2px; }
  .info-content .phone-icon { margin-right: 6px; }
  .social { display: flex; gap: 3px; margin-left: 26px; }
  .social span { width: 15px; height: 15px; border: 1.3px solid var(--white); border-radius: 50%; }

  .main-nav { position: absolute; top: 74px; left: 265px; display: flex; gap: 14.5px; font-family: "Roboto Condensed", "Arial Narrow", sans-serif; font-weight: 700; font-size: 10.6px; color: #111; }
  .main-nav a { color: inherit; text-decoration: none; padding-bottom: 4px; }
  .main-nav a.active { border-bottom: 2.5px solid var(--brand-green); }

  .hero { position: absolute; left: 10px; top: 102px; width: 840px; height: 397px; background: var(--hero-fill); }
  .hero-shadow { position: absolute; left: 30px; top: 499px; width: 800px; height: 14px;
    background: radial-gradient(ellipse at top, rgba(0,0,0,0.22), rgba(0,0,0,0) 70%); }

  .section-title { position: absolute; left: 0; width: 859px; display: flex; justify-content: center; align-items: center; gap: 16px; font-family: "Nunito Sans", Arial, sans-serif; font-weight: 800; color: var(--ink); }
  .section-title::before, .section-title::after { content: ""; width: 66px; height: 1px; background: var(--muted-line); }
  .intro-title { top: 539px; font-size: 17.5px; }
  .intro-text { position: absolute; left: 60px; top: 591px; width: 740px; font-size: 9.2px; line-height: 14.4px; text-align: center; color: #333; }

  .contact { position: absolute; left: 10px; top: 703px; width: 840px; height: 335px; background: var(--panel); }
  .contact-title { top: 744px; font-size: 17.5px; }
  .field { position: absolute; background: var(--field); border: 1.5px solid var(--field-border); border-radius: 3px; font-family: "Nunito Sans", Arial, sans-serif; font-weight: 700; font-size: 11px; color: #333; padding: 10px 11px; }
  .field-name { left: 82px; top: 795px; width: 225px; height: 33px; }
  .field-email { left: 317px; top: 795px; width: 225px; height: 33px; }
  .field-subject { left: 552px; top: 795px; width: 225px; height: 33px; }
  .field-message { left: 82px; top: 838px; width: 695px; height: 96px; }
  .send-button { position: absolute; left: 362px; top: 944px; width: 136px; height: 30px; background: var(--brand-green); border-radius: 5px; color: var(--white); font-family: "Nunito Sans", Arial, sans-serif; font-weight: 800; font-size: 11px; display: flex; align-items: center; justify-content: center; box-shadow: 0 1px 0 var(--brand-green-dark); }

  .footer-tab { position: absolute; left: 288px; top: 1012px; width: 286px; height: 27px; }
  .site-footer .brand { left: 50%; transform: translateX(-50%); top: 1062px; }
  .copyright { position: absolute; top: 1159px; width: 859px; text-align: center; font-size: 8px; font-weight: 700; color: #333; }
</style>
</head>
<body>
  <header class="site-header">
    <div class="brand"><span class="brand-mark"></span><span class="brand-name">TIDY TUB</span></div>

    <div class="info-band">
      <svg class="band" width="352" height="26" viewBox="0 0 352 26"><polygon points="0,0 352,0 328,26 24,26" fill="#0d5a2a"/></svg>
      <div class="info-content">
        <svg class="phone-icon" width="15" height="15" viewBox="0 0 16 16"><circle cx="8" cy="8" r="7.2" fill="none" stroke="#fff" stroke-width="1.3"/><path d="M5.4 4.3l1.3-.3.8 1.9-.9.7c.4.9 1.1 1.6 2 2l.7-.9 1.9.8-.3 1.3c-2.9.2-5.7-2.6-5.5-5.5z" fill="#fff"/></svg>
        FOR INFORMATION : (03) 555 0187
        <div class="social" aria-label="Social links"><span></span><span></span><span></span></div>
      </div>
    </div>

    <nav class="main-nav">
      <a class="active" href="#">HOME</a>
      <a href="#">PRODUCT RANGE</a>
      <a href="#">COLLECTION AREA</a>
      <a href="#">PAY MY ACCOUNT</a>
      <a href="#">CHANGE BIN SIZE</a>
      <a href="#">FAQ</a>
      <a href="#">ABOUT US</a>
      <a href="#">CONTACT</a>
    </nav>
  </header>

  <div class="hero" role="img" aria-label="Photo of a row of colourful recycling bins"></div>
  <div class="hero-shadow"></div>

  <h2 class="section-title intro-title">Proud to be Nelson owned and operated!</h2>
  <p class="intro-text">Lorem ipsum dolor sit amet, consectetuer adipiscing elit, sed diam nonummy nibh euismod tincidunt ut laoreet dolore magna aliquam erat volutpat. Ut wisi enim ad minim veniam, quis nostrud exerci tation ullamcorper suscipit lobortis nisl ut aliquip ex ea commodo consequat. Duis autem vel eum iriure dolor in hendrerit in vulputate velit esse molestie consequat, vel illum dolore eu feugiat nulla facilisis at vero eros et accumsan et iusto odio dignissim qui blandit praesent luptatum zzril delenit augue duis dolore te feugait nulla facilisi. Nam liber tempor cum soluta nobis eleifend option congue nihil imperdiet doming id quod mazim placerat facer possim assum. Typi non habent claritatem insitam; est usus legentis in iis qui facit eorum claritatem. Investigationes demonstraverunt lectores legere me lius quod ii legunt saepius.</p>

  <section class="contact"></section>
  <h2 class="section-title contact-title">Contact Us</h2>
  <div class="field field-name">Your Name</div>
  <div class="field field-email">Your Email</div>
  <div class="field field-subject">Your Subject</div>
  <div class="field field-message">Message</div>
  <div class="send-button">SEND YOUR MESSAGE</div>

  <svg class="footer-tab" width="286" height="27" viewBox="0 0 286 27"><path d="M0 27 C12 27 14 18 22 9 C28 2 34 0 44 0 L242 0 C252 0 258 2 264 9 C272 18 274 27 286 27 Z" fill="#ffffff"/></svg>

  <footer class="site-footer">
    <div class="brand"><span class="brand-mark"></span><span class="brand-name">TIDY TUB</span></div>
    <p class="copyright">© 2017 TIDY TUB I ALL RIGHTS RESERVED</p>
  </footer>
</body>
</html>
```